Modernize Police Fraternity Website

We're in search of a web developer to rejuvenate the digital presence of our co-ed fraternity at Marlowe Crest State, which is dedicated to supporting students pursuing careers in criminal justice and law enforcement. We aim for a modern, minimalist website that's both user-friendly and simple to maintain. Key features will include an inviting landing page, an easy-to-use contact form, and a secure online store for handling memberships, donations, and sales of items like t-shirts. While we're eager to retain as much of our existing content as possible, we're also open to thoughtful content adjustments to elevate our design. For a glimpse of our current website and to understand our mission, please visit ravelumtheta.example.

Target Market(s)

Students

Coding

Number of Pages Required

4 page

Font styles to use
Serif

Colors

Designer to choose colors to be used in the design.

Requirements
Must have
• Landing page, contact us, shop
Nice to have
• membership tracking

```html
<!DOCTYPE html>
<html lang="en">
<head>
<meta charset="utf-8">
<title>Ravelum Theta Fraternity</title>
<link rel="stylesheet" href="https://fonts.googleapis.com/css2?family=Cinzel:wght@500;600;700&family=Nunito+Sans:wght@400;600&display=swap">
<style>
:root{
  --maroon:#7b1a0f;
  --ink:#151515;
  --text:#3a3a3a;
  --paper:#ffffff;
  --mist:#f4f4f4;
  --panel:#e4e4e4;
  --black:#000000;
}
*{box-sizing:border-box;margin:0;padding:0}
html,body{width:1200px;height:3380px;overflow:hidden}
body{font-family:"Nunito Sans",sans-serif;color:var(--text);background:var(--paper);position:relative}

/* header */
.site-header{position:absolute;top:0;left:0;width:1200px;height:79px;background:var(--paper);z-index:5}
.social{position:absolute;left:112px;top:23px;display:flex;gap:8px}
.social span{width:31px;height:31px;border-radius:50%;background:#ececec;display:block}
.social span:first-child{background:var(--maroon)}
.head-address{position:absolute;left:295px;top:19px;display:flex;gap:12px;align-items:center;font-size:13px;line-height:19px;color:var(--ink)}
.pin-dot{width:34px;height:34px;border-radius:50%;background:var(--maroon);display:flex;align-items:center;justify-content:center}
.main-nav{position:absolute;right:111px;top:27px;display:flex;gap:28px;font-size:15px;color:var(--ink)}
.main-nav span{color:var(--ink)}
.crest-tab{position:absolute;left:530px;top:0;width:140px;height:155px;background:var(--paper);border-radius:0 0 70px 70px;z-index:6;display:flex;align-items:center;justify-content:center;text-align:center}
.crest-tab b{font-family:"Cinzel",serif;font-weight:700;color:var(--maroon);font-size:17px;line-height:21px}

/* hero */
.hero{position:absolute;top:79px;left:0;width:1200px;height:599px;overflow:hidden}
.hero-photo{position:absolute;inset:0;background:linear-gradient(180deg,#8d8880 0%,#6f685f 45%,#4e463f 100%)}
.hero-shade{position:absolute;inset:0;background:rgba(70,55,45,.35)}
.hero-title{position:absolute;top:215px;left:0;width:1200px;text-align:center;font-family:"Cinzel",serif;font-weight:600;color:var(--paper);font-size:62px;line-height:76px}
.hero-est{position:absolute;top:373px;left:0;width:1200px;text-align:center;font-family:"Cinzel",serif;color:var(--maroon);font-size:19px;font-weight:600}

/* about */
.about{position:absolute;top:678px;left:0;width:1200px;height:633px;background:var(--paper)}
.about-photo{position:absolute;left:145px;top:60px;width:420px;height:497px;background:linear-gradient(160deg,#6d6a66,#8a6f68 55%,#7d2a2e);clip-path:polygon(0 12%,35% 0,65% 0,100% 12%,100% 60%,50% 100%,0 60%)}
.eyebrow{font-family:"Cinzel",serif;color:var(--maroon);font-size:19px;font-weight:600}
.heading{font-family:"Cinzel",serif;color:var(--ink);font-size:36px;font-weight:600;line-height:44px}
.about-copy{position:absolute;left:625px;top:78px;width:460px}
.about-copy p{font-size:15px;line-height:30px;margin-top:20px}
.about-copy p+p{margin-top:30px}
.btn{display:inline-block;font-family:"Cinzel",serif;font-weight:700;font-size:15px;padding:0 27px;height:56px;line-height:56px;border-radius:5px;background:var(--maroon);color:var(--paper)}
.about-copy .btn{margin-top:24px}

/* store */
.store{position:absolute;top:1311px;left:0;width:1200px;height:534px;background:var(--mist);text-align:center}
.store .eyebrow{margin-top:48px}
.cards{position:absolute;left:111px;top:153px;display:flex;gap:14px}
.card{width:234px;height:305px;border:11px solid var(--maroon);border-radius:26px;background:var(--paper);padding:7px}
.card-inner{height:100%;background:var(--panel);border-radius:12px;position:relative}
.product{position:absolute;left:25px;top:18px;width:148px;height:160px;border-radius:8px}
.card small{position:absolute;left:0;right:0;top:199px;font-family:"Cinzel",serif;font-size:11px;font-weight:600;color:var(--ink)}
.card strong{position:absolute;left:0;right:0;top:217px;font-family:"Cinzel",serif;font-size:19px;font-weight:600;color:var(--ink)}

/* membership */
.support{position:absolute;top:1845px;left:0;width:1200px;height:478px;overflow:hidden}
.support-photo{position:absolute;inset:0;background:linear-gradient(110deg,#9a948c,#7a736a 60%,#8c8782)}
.support-veil{position:absolute;inset:0;background:rgba(120,110,100,.55)}
.support-red{position:absolute;inset:0;background:rgba(123,26,15,.9);clip-path:polygon(0 0,632px 0,505px 100%,0 100%)}
.support-col{position:absolute;top:92px;width:360px;text-align:center;color:var(--paper)}
.support-col h2{font-family:"Cinzel",serif;font-size:38px;font-weight:600}
.support-col p{font-size:15px;line-height:30px;margin-top:14px}
.support-col .btn{margin-top:26px;height:48px;line-height:48px;font-size:14px}
.btn.light{background:var(--paper);color:var(--maroon)}

/* contact */
.contact{position:absolute;top:2323px;left:0;width:1200px;height:644px;overflow:hidden;text-align:center}
.contact-photo{position:absolute;inset:0;background:linear-gradient(180deg,#cfc8c0,#bdb4aa)}
.contact-veil{position:absolute;inset:0;background:rgba(255,255,255,.86)}
.contact .eyebrow{position:relative;margin-top:70px}
.contact .heading{position:relative}
.info-row{position:absolute;top:183px;left:0;width:1200px}
.info{position:absolute;display:flex;gap:16px;text-align:left;font-size:15px;line-height:25px;color:var(--ink)}
.info .pin-dot{width:46px;height:46px;flex:none}
.field{position:absolute;border-bottom:1px solid #555;text-align:left;font-size:16px;color:var(--ink);padding-bottom:14px}
.submit{position:absolute;left:528px;top:508px;width:142px;height:55px;border-radius:28px;background:var(--maroon);color:var(--paper);font-family:"Cinzel",serif;font-weight:700;font-size:15px;line-height:55px}

/* footer */
.site-footer{position:absolute;top:2967px;left:0;width:1200px;height:413px;background:var(--black);color:var(--paper)}
.foot-title{font-family:"Cinzel",serif;font-weight:700;font-size:17px;white-space:nowrap}
.quick{position:absolute;left:110px;top:70px}
.quick ul{list-style:none;margin-top:16px;font-size:13px;line-height:30px}
.news{position:absolute;left:275px;top:70px;width:320px}
.news p{font-size:14px;line-height:24px;margin-top:16px;width:290px}
.news .input{margin-top:16px;width:273px;height:42px;border:1px solid var(--paper);border-radius:21px;font-size:14px;line-height:40px;padding-left:20px;position:relative}
.news .input i{position:absolute;right:4px;top:4px;width:32px;height:32px;border-radius:50%;background:var(--maroon)}
.foot-contact{position:absolute;left:610px;top:70px;font-size:14px}
.foot-contact div{display:flex;gap:14px;margin-top:16px;line-height:22px;align-items:flex-start}
.foot-contact svg{margin-top:5px}
.foot-mark{position:absolute;left:890px;top:60px;width:180px;height:180px;border-radius:50%;border:3px solid var(--maroon);display:flex;align-items:center;justify-content:center;text-align:center;font-family:"Cinzel",serif;font-weight:700;font-size:22px;line-height:28px;color:var(--maroon)}
.foot-rule{position:absolute;left:110px;right:110px;top:309px;border-top:1px solid #222}
.copyright{position:absolute;top:352px;left:0;width:1200px;text-align:center;font-size:15px}
</style>
</head>
<body>

<header class="site-header">
  <div class="social"><span></span><span></span><span></span><span></span></div>
  <div class="head-address">
    <div class="pin-dot"><svg width="12" height="16" viewBox="0 0 12 16"><path d="M6 0a6 6 0 0 0-6 6c0 4.5 6 10 6 10s6-5.5 6-10a6 6 0 0 0-6-6zm0 8.3A2.3 2.3 0 1 1 6 3.7a2.3 2.3 0 0 1 0 4.6z" fill="#fff"/></svg></div>
    <div>418 Alder Row<br>Marlowe Crest, California</div>
  </div>
  <nav class="main-nav"><span>Home</span><span>About Us</span><span>Join Us</span><span>Events</span><span>Alumni</span></nav>
</header>
<div class="crest-tab"><b>Ravelum<br>Theta</b></div>

<section class="hero">
  <div class="hero-photo" role="img" aria-label="Group of graduating members in caps and gowns in front of a campus building"></div>
  <div class="hero-shade"></div>
  <h1 class="hero-title">RAVELUM THETA<br>FRATERNITY</h1>
  <div class="hero-est">~EST 1935~</div>
</section>

<section class="about">
  <div class="about-photo" role="img" aria-label="Members standing at a recruitment table on campus"></div>
  <div class="about-copy">
    <div class="eyebrow">ABOUT US</div>
    <h2 class="heading">RAVELUM THETA</h2>
    <p>Ravelum Theta is the coeducational professional criminal justice fraternity at the acclaimed Marlowe Crest State University in beautiful Marlowe Crest, California.</p>
    <p>Student members are individuals, of varying majors, with career goals in the criminal justice system such as law enforcement, probation, corrections, security, and law. The primary objectives of the Fraternity are to assist members with occupational preparation, career selection, career acquisition and to provide a fertile environment for academic study.</p>
    <span class="btn">Learn More</span>
  </div>
</section>

<section class="store">
  <div class="eyebrow">SALES OF ITEMS</div>
  <h2 class="heading">ONLINE STORE</h2>
  <div class="cards">
    <div class="card"><div class="card-inner"><div class="product" role="img" aria-label="Black t-shirt" style="background:radial-gradient(circle,#111 55%,transparent 70%)"></div><small>MOST POPULAR</small><strong>RAVELUMTHETA</strong></div></div>
    <div class="card"><div class="card-inner"><div class="product" role="img" aria-label="Grey sweatshirt" style="background:radial-gradient(circle,#cfcfcf 55%,transparent 70%)"></div><small>MOST POPULAR</small><strong>RAVELUMTHETA</strong></div></div>
    <div class="card"><div class="card-inner"><div class="product" role="img" aria-label="Light blue t-shirt" style="background:radial-gradient(circle,#74b3d3 55%,transparent 70%)"></div><small>MOST POPULAR</small><strong>RAVELUMTHETA</strong></div></div>
    <div class="card"><div class="card-inner"><div class="product" role="img" aria-label="Sand coloured t-shirt" style="background:radial-gradient(circle,#d8cbb2 55%,transparent 70%)"></div><small>MOST POPULAR</small><strong>RAVELUMTHETA</strong></div></div>
  </div>
</section>

<section class="support">
  <div class="support-photo" role="img" aria-label="Members gathered together in matching fraternity shirts"></div>
  <div class="support-veil"></div>
  <div class="support-red"></div>
  <div class="support-col" style="left:131px">
    <h2>MEMBERSHIPS</h2>
    <p>Lorem ipsum dolor sit amet, consectetur adipiscing elit, sed do eiusmod tempor incididunt ut labore et dolore magna aliqua. Quis ipsum suspendisse ultrices gravida. Risus commodo viverra maecenas accumsan lacus vel facilisis.</p>
    <span class="btn light">Learn More</span>
  </div>
  <div class="support-col" style="left:725px">
    <h2>DONATIONS</h2>
    <p>Lorem ipsum dolor sit amet, consectetur adipiscing elit, sed do eiusmod tempor incididunt ut labore et dolore magna aliqua. Quis ipsum suspendisse ultrices gravida. Risus commodo viverra maecenas accumsan lacus vel facilisis.</p>
    <span class="btn">Donate Now</span>
  </div>
</section>

<section class="contact">
  <div class="contact-photo" role="img" aria-label="Students talking around a table in a meeting"></div>
  <div class="contact-veil"></div>
  <div class="eyebrow">GET A QUOTE</div>
  <h2 class="heading">CONTACT US</h2>
  <div class="info-row">
    <div class="info" style="left:234px"><div class="pin-dot"><svg width="14" height="19" viewBox="0 0 12 16"><path d="M6 0a6 6 0 0 0-6 6c0 4.5 6 10 6 10s6-5.5 6-10a6 6 0 0 0-6-6zm0 8.3A2.3 2.3 0 1 1 6 3.7a2.3 2.3 0 0 1 0 4.6z" fill="#fff"/></svg></div><div>VISIT US<br>418 Alder Row Marlowe<br>Crest, California</div></div>
    <div class="info" style="left:522px"><div class="pin-dot"><svg width="18" height="18" viewBox="0 0 24 24"><path d="M6.6 10.8a15 15 0 0 0 6.6 6.6l2.2-2.2a1 1 0 0 1 1-.25 11.4 11.4 0 0 0 3.6.57 1 1 0 0 1 1 1V20a1 1 0 0 1-1 1A17 17 0 0 1 3 4a1 1 0 0 1 1-1h3.5a1 1 0 0 1 1 1c0 1.25.2 2.45.57 3.57a1 1 0 0 1-.25 1z" fill="#fff"/></svg></div><div>Phone<br>+1 555 014 2280</div></div>
    <div class="info" style="left:755px"><div class="pin-dot"><svg width="18" height="14" viewBox="0 0 18 14"><rect width="18" height="14" rx="2" fill="#fff"/><path d="M1 2l8 6 8-6" fill="none" stroke="#7b1a0f" stroke-width="1.6"/></svg></div><div>Email<br>info@ravelumtheta.example</div></div>
  </div>
  <div class="field" style="left:215px;top:318px;width:368px">Name</div>
  <div class="field" style="left:615px;top:318px;width:368px">Email</div>
  <div class="field" style="left:215px;top:394px;width:770px;height:107px">Type Your Message Here....</div>
  <div class="submit">SUBMIT</div>
</section>

<footer class="site-footer">
  <div class="quick"><div class="foot-title">Quick Links</div>
    <ul><li>Home</li><li>About Us</li><li>Join Us</li><li>Events</li><li>Alumni</li></ul></div>
  <div class="news"><div class="foot-title">Subscribe To Our Newsletter</div>
    <p>Lorem ipsum dolor sit amet, consectetur adipiscing elit, sed do</p>
    <div class="input">Enter Your Email<i></i></div></div>
  <div class="foot-contact"><div class="foot-title">Contact Us</div>
    <div><svg width="10" height="14" viewBox="0 0 12 16"><path d="M6 0a6 6 0 0 0-6 6c0 4.5 6 10 6 10s6-5.5 6-10a6 6 0 0 0-6-6z" fill="#fff"/></svg><span>418 Alder Row<br>Marlowe Crest, California</span></div>
    <div><svg width="14" height="11" viewBox="0 0 18 14"><rect width="18" height="14" rx="2" fill="#fff"/></svg><span>info@ravelumtheta.example</span></div>
    <div><svg width="13" height="13" viewBox="0 0 24 24"><path d="M6.6 10.8a15 15 0 0 0 6.6 6.6l2.2-2.2a1 1 0 0 1 1-.25 11.4 11.4 0 0 0 3.6.57 1 1 0 0 1 1 1V20a1 1 0 0 1-1 1A17 17 0 0 1 3 4a1 1 0 0 1 1-1h3.5a1 1 0 0 1 1 1c0 1.25.2 2.45.57 3.57a1 1 0 0 1-.25 1z" fill="#fff"/></svg><span>+1 555 014 2280</span></div></div>
  <div class="foot-mark">Ravelum<br>Theta</div>
  <div class="foot-rule"></div>
  <div class="copyright">©Copyrights 2023 &nbsp; Ravelum Theta &nbsp; | &nbsp; All Rights Reserved</div>
</footer>

</body>
</html>
```